Professional Services/Construction Management (Millwork) Biz Cards

We've decided on a logo and have our color palette set, now we want to design some very professional looking cards that make a strong first impression - they'll reflect our tagline (that we're going to put on the back: Innovative. Professional. Leaders.

The example business card shows generally the direction we've been thinking of going for the back side - **but we're open to other ideas**

Target Market(s)

The cards should target more high-end (wealthy) owners and general contracting companies. We want them to convey a strong first impression - in a professional and not garish way.

Industry/Entity Type

Construction Company

Contact Information for Business Card

There needs to be a place for our company contractor's license number and business address. We want to also have people's names, titles, phone number, email address. The back can be the logo, tagline and web address

Requirements
Must have
• follow our color palette
Nice to have
• Font & Styles should compliment the Harbor Joinery fonts, but not necessarily match exactly

```html
<!DOCTYPE html>
<html lang="en">
<head>
<meta charset="UTF-8">
<title>Harbor Joinery Business Cards</title>
<link href="https://fonts.googleapis.com/css2?family=Saira:wght@400;500;600;700&display=swap" rel="stylesheet">
<style>
  :root {
    --page-bg: #ffffff;
    --navy: #1e3160;
    --earth: #5f5042;
    --green: #559b3f;
    --white: #ffffff;
    --rule: rgba(255, 255, 255, 0.22);
  }
  * { box-sizing: border-box; margin: 0; padding: 0; }
  html, body {
    width: 1200px;
    height: 1064px;
    overflow: hidden;
    background: var(--page-bg);
    font-family: "Saira", "Arial", sans-serif;
  }
  .canvas { position: relative; width: 1200px; height: 1064px; }
  .card {
    position: absolute;
    top: 250px;
    width: 328px;
    height: 558px;
    text-align: center;
  }
  .card--front { left: 227px; background: var(--navy); }
  .card--back { left: 643px; background: var(--earth); }

  .brand {
    position: absolute;
    top: 110px;
    left: 0;
    width: 100%;
    display: flex;
    flex-direction: column;
    align-items: center;
    gap: 14px;
  }
  .brand__disc {
    width: 44px;
    height: 44px;
    border-radius: 50%;
    background: var(--earth);
  }
  .brand__name {
    color: var(--green);
    font-weight: 700;
    font-size: 27px;
    line-height: 1.05;
    letter-spacing: 1px;
    text-transform: uppercase;
  }
  .tagline {
    position: absolute;
    top: 326px;
    width: 100%;
    color: var(--green);
    font-weight: 700;
    font-size: 21px;
    line-height: 28px;
    text-transform: uppercase;
  }
  .website {
    position: absolute;
    top: 510px;
    width: 100%;
    color: var(--white);
    font-weight: 700;
    font-size: 15.5px;
  }

  .person { position: absolute; top: 204px; width: 100%; }
  .person__name {
    color: var(--white);
    font-weight: 700;
    font-size: 22px;
    line-height: 26px;
    letter-spacing: 0.5px;
  }
  .person__title {
    color: var(--green);
    font-weight: 700;
    font-size: 15px;
    line-height: 20px;
  }
  .contact {
    position: absolute;
    top: 325px;
    left: 33px;
    width: 262px;
    list-style: none;
    color: var(--white);
  }
  .contact__item {
    font-size: 14.5px;
    height: 39px;
    line-height: 38px;
    border-bottom: 1px solid var(--rule);
  }
  .contact__item--address {
    border-bottom: none;
    font-size: 11px;
    line-height: 16px;
    height: auto;
    padding-top: 6px;
  }
  .license {
    position: absolute;
    top: 506px;
    width: 100%;
    color: var(--green);
    font-weight: 400;
    font-size: 18px;
    letter-spacing: 0.3px;
  }
</style>
</head>
<body>
<main class="canvas">
  <section class="card card--front" aria-label="Card front">
    <div class="brand">
      <span class="brand__disc" aria-hidden="true"></span>
      <p class="brand__name">Harbor<br>Joinery</p>
    </div>
    <p class="tagline">Innovative<br>Professional<br>Leaders</p>
    <p class="website">www.harborjoinery.com</p>
  </section>

  <section class="card card--back" aria-label="Card back">
    <div class="person">
      <p class="person__name">ROSS DELANEY</p>
      <p class="person__title">PRESIDENT - FOUNDER</p>
    </div>
    <ul class="contact">
      <li class="contact__item">Office Phone 123-456-7890</li>
      <li class="contact__item">Cell Phone 123-456-7890</li>
      <li class="contact__item">E-mail: name@harborjoinery.com</li>
      <li class="contact__item contact__item--address">Office Address: Maple Ridge, Oregon, near the<br>intersection of Route 4 and Elm Boulevard</li>
    </ul>
    <p class="license">LICENSE # 000000</p>
  </section>
</main>
</body>
</html>
```